Energy cost saving website (job description rewritten!)

Job Type: WordPress design
Task Outline: Create a WordPress design
Task Description:
We are new business (Germany) in the market of saving costs by power-saving (name: 'wir-falten-eure-Wolkenbögen.de'). This is reached by changing the supplier, the use of LED bulbs, energy saving washing machines, stoves, microwaves, hairdryers, vacuum cleaners and the like - where all of these be selled or affiliated through the website maybe you will create for us.
Design parameters:
We want a serious design that embodies a feeling of honesty, competence and capability.
Visitors should particularly see that this site saves them money!
The home page mainly should act as a selector of possibilities saving money by power-saving, usage of LED bulbs and large energy saving household devices (washing machines, etc.)
Updates
Hello designers,
browsing through the PixelHarbors files of portfolios I found one header graphics which excites me. Please find it here: http://www.pixelharbor-example.net/design/482716/wordpress-design-by-tarek-olumide . Note: it is NOT the picture but the shadowing. So if you consider this in your concepts would be another 'nice-to-have'.
Thanks.
Target Market(s)
People looking out for saving money by power-saving.
Industry/Entity Type
Business
Requirements
Must have
- Look and feel of 'this site saves me money'!
Nice to have
- We love 3D effects, but its not a must have. We also like cartoons, but feel free to develop your own concept, please. An appropriate backgrond picture would be nice.
Should not have
- Some kind of these exaggerated smiling or handshaking photos. That bathetic symbols like money bills or coins stacks.

```html
<!DOCTYPE html>
<html lang="en">
<head>
<meta charset="utf-8">
<title>wir-falten-eure-Wolkenbögen.de</title>
<link rel="stylesheet" href="https://fonts.googleapis.com/css2?family=Cabin:wght@400;500;600;700&family=Arimo:wght@400&display=swap">
<style>
  :root {
    --orange-deep: #ff6400;
    --orange-mid: #ff9c00;
    --orange-text: #ff6a00;
    --panel: #e6e7e8;
    --ink: #1b1b1b;
    --ink-soft: #3a3a3a;
    --body-grey: #8a8a8a;
    --white: #ffffff;
    --rule: #d3d4d6;
  }
  * { margin: 0; padding: 0; box-sizing: border-box; }
  html, body { width: 980px; height: 1200px; overflow: hidden; }
  body { position: relative; background: var(--panel); font-family: "Arimo", Arial, sans-serif; }

  .masthead {
    position: absolute; left: 0; top: 0; width: 980px; height: 672px;
    background: linear-gradient(180deg, var(--orange-deep) 0%, var(--orange-mid) 40%, var(--orange-mid) 55%, var(--orange-deep) 100%);
  }
  .site-name {
    position: absolute; left: 110px; top: 34px;
    font-family: "Cabin", sans-serif; font-weight: 600; font-size: 24px;
    color: var(--white); letter-spacing: -0.3px;
  }

  .hero-shadow {
    position: absolute; left: 130px; top: 404px; width: 720px; height: 30px;
    background: radial-gradient(ellipse at 50% 30%, rgba(0,0,0,0.75) 0%, rgba(0,0,0,0.45) 45%, rgba(0,0,0,0) 72%);
    filter: blur(3px);
  }
  .hero {
    position: absolute; left: 110px; top: 88px; width: 760px; height: 322px;
    background: var(--panel);
  }
  .hero-photo {
    position: absolute; left: 39px; top: 31px; width: 405px; height: 246px;
    background: radial-gradient(ellipse at 45% 50%, #f4f4f4 0%, #dcdcdc 55%, #e3e4e5 100%);
  }
  .hero-copy { position: absolute; left: 467px; top: 78px; width: 280px; }
  .hero-title {
    font-family: "Cabin", sans-serif; font-weight: 700; font-size: 21.5px; line-height: 25px;
    color: var(--orange-text); text-transform: uppercase; letter-spacing: 0.2px;
  }
  .hero-lead {
    margin-top: 6px;
    font-family: "Cabin", sans-serif; font-weight: 400; font-size: 19.5px; line-height: 24px;
    color: var(--ink-soft);
  }
  .btn-learn {
    position: absolute; left: 464px; top: 213px; width: 109px; height: 35px;
    border-radius: 4px;
    background: linear-gradient(180deg, #ff9a2a 0%, #ff6a00 100%);
    color: var(--white); font-family: "Cabin", sans-serif; font-size: 16px;
    line-height: 35px; text-align: center;
  }

  .feature { position: absolute; top: 449px; width: 224px; }
  .feature-photo {
    position: relative; width: 224px; height: 144px;
    border: 2px solid #f4f4f4; border-radius: 3px;
  }
  .feature-photo::after {
    content: ""; position: absolute; left: 4px; right: 4px; bottom: -9px; height: 8px;
    background: radial-gradient(ellipse at 50% 0%, rgba(0,0,0,0.7) 0%, rgba(0,0,0,0) 75%);
  }
  .feature-label {
    margin-top: 22px; text-align: center;
    font-family: "Cabin", sans-serif; font-size: 28px; color: var(--white);
  }
  .feature-label .chev { font-size: 26px; font-weight: 700; }
  .f-energy { left: 110px; }
  .f-energy .feature-photo { background: linear-gradient(120deg, #d9d6d0 0%, #c9a27f 40%, #3aa7c2 70%, #e7e7e7 100%); }
  .f-bills { left: 376px; }
  .f-bills .feature-photo { background: linear-gradient(90deg, #bfe6f7 0%, #3a3d40 25%, #e9e9e9 45%, #2a2c2e 55%, #ededed 75%, #bfe6f7 100%); }
  .f-tech { left: 645px; }
  .f-tech .feature-photo { background: radial-gradient(ellipse at 55% 55%, #f7f7f7 0%, #c9c9c9 45%, #e3e4e5 75%); }

  .article { position: absolute; left: 125px; top: 708px; width: 424px; }
  .article-title {
    font-family: "Cabin", sans-serif; font-weight: 400; font-size: 22px; color: var(--ink);
    margin-bottom: 8px;
  }
  .article p {
    font-size: 12px; line-height: 20.4px; color: var(--body-grey); text-align: justify;
  }
  .article p + p { margin-top: 29px; }

  .sidebar { position: absolute; left: 594px; top: 706px; width: 275px; }
  .side-item { padding-bottom: 15px; }
  .side-item + .side-item { border-top: 1px solid var(--rule); padding-top: 12px; }
  .side-title {
    font-family: "Cabin", sans-serif; font-weight: 400; font-size: 23px; color: var(--orange-text);
    margin-bottom: 6px;
  }
  .side-item p { font-size: 11.5px; line-height: 18.8px; color: var(--body-grey); }

  .footer {
    position: absolute; left: 0; top: 1112px; width: 980px; height: 88px;
    background: linear-gradient(180deg, #ff8a00 0%, var(--orange-mid) 45%, #ff8200 100%);
  }
  .footer-nav {
    position: absolute; left: 127px; top: 32px;
    font-size: 10.2px; color: var(--ink);
  }
  .footer-nav span { margin: 0 5px; }
  .footer-brand {
    position: absolute; left: 600px; top: 20px;
    font-family: "Cabin", sans-serif; font-weight: 600; font-size: 18px; color: var(--ink);
    letter-spacing: -0.3px;
  }
  .copyright { position: absolute; left: 603px; top: 48px; font-size: 10.2px; color: var(--ink); }
</style>
</head>
<body>
  <header class="masthead">
    <div class="site-name">wir-falten-eure-Wolkenbögen.de</div>

    <div class="hero-shadow"></div>
    <section class="hero">
      <div class="hero-photo" role="img" aria-label="Photo of an LED light bulb lying on its side"></div>
      <div class="hero-copy">
        <h1 class="hero-title">How to save money<br>with electricity</h1>
        <p class="hero-lead">Review your current home energy usage and save more.</p>
      </div>
      <div class="btn-learn">Learn more</div>
    </section>

    <div class="feature f-energy">
      <div class="feature-photo" role="img" aria-label="Photo of a family loading a washing machine"></div>
      <div class="feature-label">Save Energy <span class="chev">»</span></div>
    </div>
    <div class="feature f-bills">
      <div class="feature-photo" role="img" aria-label="Photo of two analogue power meters"></div>
      <div class="feature-label">Cut high bills <span class="chev">»</span></div>
    </div>
    <div class="feature f-tech">
      <div class="feature-photo" role="img" aria-label="Photo of energy saving light bulbs"></div>
      <div class="feature-label">Technology <span class="chev">»</span></div>
    </div>
  </header>

  <main>
    <article class="article">
      <h2 class="article-title">Cut Electricity Bills and help save the planet</h2>
      <p>Are your electricity bills getting higher and higher even though you are using the same amount of electricity? No, your electrical company is not overcharging you if that is what you are perhaps thinking. In fact, most homeowners get “high blood pressure“ each month when they see their electricity bills. However, they do nothing about it which is the main problem. The thing is that electricity bills most certainly will not get any lower and complaining about the costs of electricity will not help. This is due to the fact that electricity is predominantly generated from fossil fuels which are slowly running out. As a result, electricity bills will only continue to rise and the same counts for carbon dioxide emissions which are the number one cause of the global climate change.</p>
      <p>Reducing your electricity consumption is the only way to cut your electricity bills and reduce your carbon footprint at the same time. But how you are supposed to save electricity when just about everything in your home is powered by electricity?</p>
    </article>

    <aside class="sidebar">
      <div class="side-item">
        <h3 class="side-title">Lorem Ipsum dolor</h3>
        <p>Lorem ipsum dolor sit amet, consectetur adipisicing elit, sed do eiusmod tempor incididunt ut labore et dolore magna aliqua.</p>
      </div>
      <div class="side-item">
        <h3 class="side-title">Lorem Ipsum dolor</h3>
        <p>Lorem ipsum dolor sit amet, consectetur adipisicing elit, sed do eiusmod tempor incididunt ut labore et dolore magna aliqua.</p>
      </div>
      <div class="side-item">
        <h3 class="side-title">Lorem Ipsum dolor</h3>
        <p>Lorem ipsum dolor sit amet, consectetur adipisicing elit, sed do eiusmod tempor incididunt ut labore et dolore magna aliqua.</p>
      </div>
    </aside>
  </main>

  <footer class="footer">
    <nav class="footer-nav">Home<span>|</span>About Us<span>|</span>News<span>|</span>Contact</nav>
    <div class="footer-brand">wir-falten-eure-Wolkenbögen.de</div>
    <div class="copyright">Copyright © 2012</div>
  </footer>
</body>
</html>
```